Fully Functional Wix Website, Not Just Images

Please read all instructions carefully. This is NOT merely a design project where the artist will deliver static images. This project requires that the designer build a fully functional SEO optimized website within Wix then transfer full ownership to me. See attached "instructions for design" file. I have wix for other websites. Only wix is acceptable. Do not submit more than 1 design per designer. If you submit more than 1 design I will award to someone else.

Target Market(s)

see attachments and brisvale482.com

Industry/Entity Type

Coding

Coded - Design and coding required

Number of Pages Required

4 page

Font styles to use
Other font styles liked:
• see attachments and brisvale482.com

Requirements
Must have
Nice to have
Should not have

```html
<!DOCTYPE html>
<html lang="en">
<head>
<meta charset="utf-8">
<title>Services | Harbor Crest Boat Training &amp; Charters</title>
<link rel="stylesheet" href="https://fonts.googleapis.com/css2?family=Michroma&family=Montserrat:wght@400;500;600;700&display=swap">
<style>
  :root {
    --gold: #d9a520;
    --ink: #111418;
    --white: #ffffff;
    --navy: #0b2147;
    --navy-deep: #08193a;
    --teal: #1f6b6f;
    --sea: #2d7f86;
    --muted: #3a3a3a;
    --card-line: #ececec;
  }
  * { margin: 0; padding: 0; box-sizing: border-box; }
  html, body { width: 960px; height: 1200px; overflow: hidden; }
  body {
    position: relative;
    font-family: "Montserrat", sans-serif;
    color: var(--ink);
    background: var(--white);
  }
  .hero-photo {
    position: absolute; left: 0; top: 0; width: 960px; height: 460px;
    background:
      radial-gradient(ellipse 420px 160px at 600px 270px, rgba(255,255,255,0.55), rgba(255,255,255,0) 70%),
      linear-gradient(180deg, #1c5560 0%, var(--teal) 30%, var(--sea) 55%, #9fc6c6 80%, var(--white) 100%);
  }
  .sea-photo {
    position: absolute; left: 0; top: 700px; width: 960px; height: 500px;
    background: linear-gradient(180deg, var(--white) 0%, #c7d3e0 14%, #4c6d98 32%, #173463 50%, var(--navy) 70%, var(--navy-deep) 100%);
  }

  .topbar { position: absolute; left: 0; top: 0; width: 960px; height: 80px; }
  .brand {
    position: absolute; left: 110px; top: 26px;
    display: flex; align-items: center; gap: 8px;
    color: var(--white); font-family: "Michroma", sans-serif; font-size: 11px; line-height: 1.3;
    width: 170px;
  }
  .brand-dot { width: 24px; height: 24px; border-radius: 50%; border: 2px solid var(--gold); flex: none; }
  .nav { position: absolute; top: 24px; left: 491px; display: flex; gap: 25px; }
  .nav a { color: var(--white); text-decoration: none; font-size: 8.8px; font-weight: 500; letter-spacing: 0.2px; line-height: 14px; }
  .nav a.is-home { font-weight: 700; }
  .nav a.is-active { color: var(--gold); }
  .nav-marker { position: absolute; left: 540px; top: 0; width: 48px; height: 2px; background: var(--gold); }
  .contact-btn {
    position: absolute; left: 767px; top: 18px; width: 83px; height: 26px;
    border: 1px solid var(--white); border-radius: 14px;
    color: var(--white); font-size: 8px; font-weight: 700; text-align: center; line-height: 24px;
    text-decoration: none;
  }

  .hero-text { position: absolute; left: 109px; top: 136px; color: var(--white); font-family: "Michroma", sans-serif; }
  .hero-kicker { font-size: 15px; letter-spacing: 0.3px; }
  .hero-title { font-size: 36px; line-height: 1; margin-top: 14px; letter-spacing: 0.3px; font-weight: 700; }
  .hero-sub { font-size: 15.5px; line-height: 20px; margin-top: 13px; font-weight: 700; }

  .services { position: absolute; left: 126px; top: 484px; display: flex; gap: 11px; }
  .service { position: relative; width: 169px; height: 203px; }
  .service-card {
    position: absolute; left: 0; top: 34px; width: 169px; height: 169px;
    background: var(--white); border: 1px solid var(--card-line); border-radius: 14px;
    box-shadow: 0 2px 10px rgba(0,0,0,0.04);
  }
  .service-badge {
    position: absolute; left: 44px; top: 0; width: 81px; height: 81px; border-radius: 50%;
    background: var(--white); border: 2px dashed var(--gold);
    display: flex; align-items: center; justify-content: center;
  }
  .service-body { position: absolute; left: 0; top: 110px; width: 169px; text-align: center; }
  .service-title { font-family: "Michroma", sans-serif; font-size: 9.6px; color: var(--ink); white-space: nowrap; letter-spacing: 0; font-weight: 700; }
  .service-desc { font-size: 8.6px; color: var(--muted); line-height: 11px; margin: 5px auto 0; width: 150px; }
  .service-btn {
    display: block; margin: 9px auto 0; width: 89px; height: 23px;
    border: 1px solid var(--ink); border-radius: 12px;
    font-size: 6.4px; font-weight: 700; line-height: 21px; color: var(--ink); text-decoration: none;
  }

  .footer { position: absolute; left: 0; top: 912px; width: 960px; color: var(--white); text-align: center; }
  .footer-rule { position: absolute; top: 59px; height: 1px; background: rgba(255,255,255,0.35); }
  .footer-brand {
    position: absolute; left: 423px; top: 2px; width: 114px; height: 114px; border-radius: 50%;
    border: 3px solid var(--gold); background: var(--navy-deep);
    display: flex; align-items: center; justify-content: center;
    font-family: "Michroma", sans-serif; font-size: 11px; line-height: 1.4; color: var(--white);
  }
  .footer-nav { position: absolute; top: 131px; left: 0; width: 960px; display: flex; justify-content: center; gap: 29px; }
  .footer-nav a { color: var(--white); text-decoration: none; font-size: 8.6px; font-weight: 600; }
  .footer-contact { position: absolute; top: 151px; left: 0; width: 960px; display: flex; justify-content: center; gap: 29px; font-size: 8.8px; }
  .footer-contact span { display: inline-flex; align-items: center; gap: 4px; }
  .social { position: absolute; top: 185px; left: 414px; display: flex; gap: 5.5px; }
  .social a { width: 29px; height: 29px; border-radius: 50%; background: var(--white); display: block; }
  .copyright { position: absolute; top: 252px; left: 0; width: 960px; font-size: 8.2px; font-weight: 700; }
</style>
</head>
<body>
  <div class="hero-photo" role="img" aria-label="Photo of a white center-console fishing boat speeding across green sea water"></div>
  <div class="sea-photo" role="img" aria-label="Photo of deep blue open ocean with sparkling surface"></div>

  <header class="topbar">
    <div class="nav-marker"></div>
    <div class="brand"><span class="brand-dot"></span><span>Harbor Crest</span></div>
    <nav class="nav">
      <a class="is-home" href="#">HOME</a>
      <a class="is-active" href="#">SERVICES</a>
      <a href="#">BOATING AIDS</a>
      <a href="#">GALLERY</a>
    </nav>
    <a class="contact-btn" href="#">CONTACT</a>
  </header>

  <section class="hero-text">
    <p class="hero-kicker">WELCOME TO</p>
    <h1 class="hero-title">SERVICES</h1>
    <p class="hero-sub">TRAINING, CAPTAINING<br>&amp; DELIVERIES</p>
  </section>

  <section class="services">
    <article class="service">
      <div class="service-card"></div>
      <div class="service-badge">
        <svg width="42" height="34" viewBox="0 0 42 34"><polygon points="21,2 41,11 21,20 1,11" fill="#111418"/><path d="M9 15 V24 C15 30 27 30 33 24 V15 L21 21 Z" fill="#111418"/><line x1="37" y1="13" x2="37" y2="27" stroke="#111418" stroke-width="1.5"/><circle cx="37" cy="29" r="2" fill="#111418"/></svg>
      </div>
      <div class="service-body">
        <h2 class="service-title">BOAT TRAINING</h2>
        <p class="service-desc">Hands-on instruction for new and experienced boaters.</p>
        <a class="service-btn" href="#">LEARN MORE</a>
      </div>
    </article>
    <article class="service">
      <div class="service-card"></div>
      <div class="service-badge">
        <svg width="48" height="28" viewBox="0 0 48 28"><path d="M2 16 H46 L40 24 H6 Z" fill="#111418"/><path d="M12 15 L16 9 H34 L40 15 Z" fill="#111418"/><rect x="20" y="4" width="8" height="5" fill="#111418"/><rect x="2" y="26" width="42" height="1.5" fill="#111418"/></svg>
      </div>
      <div class="service-body">
        <h2 class="service-title">CHARTER</h2>
        <p class="service-desc">Relax and explore with captain-guided charters.</p>
        <a class="service-btn" href="#">VIEW CHARTER</a>
      </div>
    </article>
    <article class="service">
      <div class="service-card"></div>
      <div class="service-badge">
        <svg width="36" height="32" viewBox="0 0 36 32"><path d="M2 3 C8 1 14 2 17 5 V30 C13 27 8 27 2 28 Z" fill="#111418"/><path d="M34 3 C28 1 22 2 19 5 V30 C23 27 28 27 34 28 Z" fill="#111418"/></svg>
      </div>
      <div class="service-body">
        <h2 class="service-title">SAFE BOATER SERIES</h2>
        <p class="service-desc">Books to help you make informed decisions on and off the water.</p>
        <a class="service-btn" href="#">SEE THE BOOKS</a>
      </div>
    </article>
    <article class="service">
      <div class="service-card"></div>
      <div class="service-badge">
        <svg width="38" height="34" viewBox="0 0 38 34"><circle cx="9" cy="9" r="5" fill="#111418"/><circle cx="29" cy="9" r="5" fill="#111418"/><circle cx="19" cy="12" r="6.5" fill="#111418"/><rect x="1" y="15" width="14" height="12" rx="5" fill="#111418"/><rect x="23" y="15" width="14" height="12" rx="5" fill="#111418"/><rect x="10" y="19" width="18" height="14" rx="6" fill="#111418"/></svg>
      </div>
      <div class="service-body">
        <h2 class="service-title">PRIVATE COACHING</h2>
        <p class="service-desc">Personalized training for your goals.</p>
        <a class="service-btn" href="#">GET STARTED</a>
      </div>
    </article>
  </section>

  <footer class="footer">
    <div class="footer-rule" style="left:121px;width:282px"></div>
    <div class="footer-rule" style="left:567px;width:282px"></div>
    <div class="footer-brand">Harbor<br>Crest</div>
    <nav class="footer-nav">
      <a href="#">HOME</a><a href="#">SERVICES</a><a href="#">BOATING AIDS</a><a href="#">GALLERY</a><a href="#">CONTACT US</a>
    </nav>
    <div class="footer-contact">
      <span><svg width="8" height="6" viewBox="0 0 8 6"><rect width="8" height="6" fill="#d9a520"/><path d="M0 0 L4 3.5 L8 0" stroke="#08193a" stroke-width="0.8" fill="none"/></svg>service@harborcrestboating.com</span>
      <span><svg width="6" height="8" viewBox="0 0 6 8"><path d="M3 8 C1 5 0 4 0 3 A3 3 0 0 1 6 3 C6 4 5 5 3 8 Z" fill="#d9a520"/><circle cx="3" cy="3" r="1" fill="#08193a"/></svg>Palm Cove, Florida</span>
      <span><svg width="8" height="8" viewBox="0 0 8 8"><path d="M1 0 L3 0 L3.5 2 L2.3 3 C3 4.5 3.5 5 5 5.7 L6 4.5 L8 5 L8 7 C8 7.5 7.5 8 7 8 C3 8 0 5 0 1 C0 0.5 0.5 0 1 0 Z" fill="#d9a520"/></svg>Text (555) 014-2276</span>
    </div>
    <div class="social">
      <a href="#" aria-label="Social link"></a><a href="#" aria-label="Social link"></a><a href="#" aria-label="Social link"></a><a href="#" aria-label="Social link"></a>
    </div>
    <div class="footer-rule" style="top:258px;left:121px;width:202px"></div>
    <div class="footer-rule" style="top:258px;left:638px;width:202px"></div>
    <p class="copyright">©2026 BY HARBOR CREST BOAT TRAINING &amp; CHARTERS, LLC</p>
  </footer>
</body>
</html>
```